Book Cover for Christian Book titled, "Lamps Along the Quiet Road"

Size of book cover will be 6" x 9".
The book is about how a person can know beyond a shadow of a doubt that they will go to heaven when they die.
The Title is "Lamps Along the Quiet Road"
Subtitle is "A Plain Guide to Lasting Peace and Steady Hope for Every Season."
The front of the book should have title, subtitle, and author. The back of the book and spine should have no text and be a solid color.
The uploaded pic is a possibility for a design; but I'm open to other designs.
Whatever images are used need to be very high quality to meet Maple Print Works guidelines. Also, the finished product needs to be sized to match the MPW guide for a 6x9 book.

```html
<!DOCTYPE html>
<html lang="en">
<head>
<meta charset="utf-8">
<title>Lamps Along the Quiet Road — Front Cover</title>
<link rel="stylesheet" href="https://fonts.googleapis.com/css2?family=Playfair+Display:wght@600;700&family=Crimson+Text:wght@600;700&display=swap">
<style>
  :root {
    --stage: #e4e4e4;
    --ink: #0d2430;
    --author: #ffffff;
    --sky-light: #eef6fa;
    --sky-blue: #6cbbdc;
    --warm-gold: #f1e07a;
    --field-green: #2f7a24;
  }
  * { margin: 0; padding: 0; box-sizing: border-box; }
  html, body { width: 1200px; height: 769px; overflow: hidden; background: var(--stage); }
  .canvas { position: relative; width: 1200px; height: 769px; }
  .cover {
    position: absolute; left: 358px; top: 42px; width: 484px; height: 686px;
    overflow: hidden;
  }
  .cover-photo-area {
    position: absolute; inset: 0;
    background: linear-gradient(180deg,
      var(--sky-light) 0%,
      var(--sky-blue) 40%,
      var(--warm-gold) 75%,
      var(--field-green) 100%);
  }
  .title {
    position: absolute; left: 0; width: 100%; text-align: center;
    font-family: "Playfair Display", Georgia, serif; font-weight: 700;
    color: var(--ink); line-height: 1; white-space: nowrap; display: block;
  }
  .title-line-1 { top: 38px; font-size: 62px; letter-spacing: 1px; }
  .title-line-2 { top: 100px; font-size: 36px; display: flex; align-items: center; justify-content: center; gap: 14px; padding: 0 54px; }
  .title-line-2 .rule { flex: 1; height: 2px; background: var(--ink); }
  .title-line-3 { top: 137px; font-size: 74px; }
  .title-line-4 { top: 203px; font-size: 104px; }
  .subtitle {
    position: absolute; left: 0; top: 430px; width: 100%; text-align: center;
    font-family: "Crimson Text", Georgia, serif; font-weight: 700;
    font-size: 22px; line-height: 27px; color: var(--ink);
  }
  .author {
    position: absolute; left: 0; top: 650px; width: 100%; text-align: center;
    font-family: "Crimson Text", Georgia, serif; font-weight: 700;
    font-size: 19px; letter-spacing: 1.5px; color: var(--author);
  }
</style>
</head>
<body>
<div class="canvas">
  <section class="cover">
    <div class="cover-photo-area" role="img" aria-label="Photograph of sunlight breaking through clouds over a green field"></div>
    <h1>
      <span class="title title-line-1">LAMPS</span>
      <span class="title title-line-2"><span class="rule"></span>ALONG THE<span class="rule"></span></span>
      <span class="title title-line-3">QUIET</span>
      <span class="title title-line-4">ROAD</span>
    </h1>
    <p class="subtitle">A Plain Guide to Lasting Peace<br>and Steady Hope for<br>Every Season.</p>
    <p class="author">AUTHOR</p>
  </section>
</div>
</body>
</html>
```